Brochure Design Project

Create a design for parent and family education program (using attached text) that can serve as a template for other brochures

Industry/Entity Type

Education

Requirements
Must have
• leave space for one logo (same logo as on attached)

```html
<!DOCTYPE html>
<html lang="en">
<head>
<meta charset="utf-8">
<title>Parent &amp; Family Education Brochure</title>
<link href="https://fonts.googleapis.com/css2?family=Arimo:wght@400;700&display=swap" rel="stylesheet">
<style>
:root{
  --navy:#1f4a86;
  --navy-deep:#163866;
  --black:#0c0c0c;
  --ink:#4a4a4a;
  --head:#2a5ea3;
  --paper:#ffffff;
  --stage:#ececec;
  --rule:#b9c6d8;
}
*{box-sizing:border-box;margin:0;padding:0}
html,body{width:808px;height:1200px;overflow:hidden}
body{background:var(--stage);font-family:"Arimo",Arial,sans-serif;position:relative}

/* covers */
.cover{position:absolute;top:50px;width:330px;height:450px;background:var(--black);overflow:hidden;color:var(--paper)}
.back-cover{left:55px}
.front-cover{left:423px}
.back-cover .side-band{position:absolute;left:0;top:0;width:64px;height:100%;background:linear-gradient(90deg,var(--navy-deep),var(--navy))}
.brand-mark{width:30px;height:30px;border:2px solid var(--paper);display:block}
.back-cover .brand-mark{position:absolute;left:17px;top:30px}
.back-cover .photo{position:absolute;left:64px;top:110px;right:0;height:270px;background:radial-gradient(ellipse at 60% 40%,#8a8a8a,#3a3a3a 55%,#111 90%)}
.back-cover .cta{position:absolute;left:80px;top:28px;right:12px;font-size:10px;line-height:1.45}
.back-cover .cta p{margin-bottom:6px}
.back-cover .cta li{list-style:none;padding-left:10px;position:relative}
.back-cover .cta li::before{content:"•";position:absolute;left:0}
.back-cover .locations{position:absolute;left:80px;right:10px;bottom:16px;font-size:7px;line-height:1.45}
.back-cover .locations strong{display:block;font-size:9px;font-weight:400;margin-bottom:3px}

.front-cover .photo{position:absolute;inset:0;background:radial-gradient(ellipse at 45% 55%,#9c9c9c,#505050 45%,#161616 85%)}
.front-cover .title-bar{position:absolute;left:30px;right:30px;top:44px;background:rgba(31,74,134,.85);padding:9px 14px;font-size:17px}
.front-cover .url{position:absolute;left:24px;bottom:28px;font-size:8px}
.front-cover .brand-box{position:absolute;right:18px;bottom:18px;background:var(--navy);padding:8px 10px;display:flex;align-items:center;gap:7px;font-size:11px;font-weight:700;line-height:1.2}
.front-cover .brand-box .brand-mark{width:18px;height:18px}

/* inside spread */
.spread{position:absolute;left:55px;top:540px;width:698px;height:600px;background:var(--paper);overflow:hidden}
.spread .panel{position:absolute;left:0;top:0;width:178px;height:100%;background:linear-gradient(90deg,var(--navy-deep),var(--navy));color:var(--paper)}
.spread .fold{position:absolute;left:178px;top:0;width:34px;height:100%;background:linear-gradient(90deg,#d5d5d5,#f4f4f4 60%,#fff)}
.panel .brand{position:absolute;left:16px;top:26px;display:flex;align-items:center;gap:8px;font-size:12px;font-weight:700;line-height:1.2}
.panel .brand .brand-mark{width:24px;height:24px}
.panel .panel-title{position:absolute;left:22px;top:195px;font-size:11px}
.panel .url{position:absolute;left:22px;bottom:24px;font-size:9px}

.hero{position:absolute;left:200px;top:14px;width:478px;height:150px;background:linear-gradient(170deg,#c8d7a8,#8fa45e 45%,#5f7030 80%,#3c4a22)}
.hero-copy{position:absolute;left:360px;top:26px;width:300px;color:var(--paper)}
.hero-copy h2{font-size:19px;font-weight:700}
.hero-copy p{font-size:9px;line-height:1.35}

.columns{position:absolute;left:210px;top:178px;right:20px;display:grid;grid-template-columns:1fr 1fr 1fr;gap:0}
.column{padding:0 10px;font-size:7px;line-height:1.38;color:var(--ink)}
.column+.column{border-left:1px solid var(--rule)}
.column h3{font-size:7.5px;color:var(--head);font-weight:700;margin-top:8px;margin-bottom:1px}
.column h3:first-child{margin-top:0}
</style>
</head>
<body>

<section class="cover back-cover">
  <div class="side-band"><span class="brand-mark"></span></div>
  <div class="photo" role="img" aria-label="Black and white photo of an adult hand holding a baby's hand"></div>
  <div class="cta">
    <p>Become a healthy, happy family today!</p>
    <p>Register or learn more about Westbrook's Parent &amp; Family Education programs:</p>
    <ul>
      <li>Call Westbrook 411 at 555-010-4411</li>
      <li>Visit familycarecenter.org</li>
    </ul>
  </div>
  <div class="locations">
    <strong>Westbrook Hospital</strong>
    Central (Park Plaza) 555-010-9610, East (Maple Grove) 555-010-2000, North (Hill City) 555-010-6227, South (Overlook) 555-010-3000
  </div>
</section>

<section class="cover front-cover">
  <div class="photo" role="img" aria-label="Black and white close-up of a baby's open hand resting in an adult's hands"></div>
  <div class="title-bar">Parent &amp; Family Education</div>
  <div class="url">www.familycarecenter.org</div>
  <div class="brand-box"><span class="brand-mark"></span><span>Westbrook<br>Women's Services</span></div>
</section>

<section class="spread">
  <div class="panel">
    <div class="brand"><span class="brand-mark"></span><span>Westbrook<br>Women's Services</span></div>
    <div class="panel-title">Parent &amp; Family Education</div>
    <div class="url">www.familycarecenter.org</div>
  </div>
  <div class="fold"></div>

  <div class="hero" role="img" aria-label="Photo of a young family sitting together on the grass in a sunny park"></div>
  <div class="hero-copy">
    <h2>Oh Baby!</h2>
    <p>Westbrook offers comprehensive health advice to keep your little one well – from birth and beyond.</p>
  </div>

  <div class="columns">
    <div class="column">
      <h3>Childbirth Preparation "All About Birth"</h3>
      <p>During All About Birth, we will help you prepare for what you might expect during your labor, birth and postpartum. Our class combines interaction with our knowledgeable childbirth educators and online resources for your continued learning. Options for participating include: <b>Two evening classes One half day Saturday class Online course</b> (note this course is taken at your convenience and does not include class time with our childbirth educators).</p>
      <h3>Breastfeeding</h3>
      <p>Get the basics you need for successful breastfeeding. This class includes techniques and tips to get you off to a good start and ideas to help fit breastfeeding into your lifestyle. Birth partners and other family members are encouraged to attend.</p>
      <h3>Breastfeeding Support: Mom2Mom</h3>
      <p>Join other mothers and their babies to share experiences, get encouragement, and learn ideas from experienced lactation consultants.</p>
      <h3>Newborn Care</h3>
      <p>Get the latest information on baby care basics, safety, early brain development and common new parent concerns in this interactive class.</p>
    </div>
    <div class="column">
      <h3>CPR-Infant-Child</h3>
      <p>From birth to age 8, learn the basic life support (BLS) skills according to Heart Safety Council (HSC) guidelines.</p>
      <h3>Infant Child First Aid: What to Do in an Emergency</h3>
      <p>This course will discuss prevention and how to avoid medical emergencies included will be hands-on first aid stations with real life scenarios for practice so that you will know what to do in an emergency.</p>
      <h3>Baby Sing and Sign</h3>
      <p>Learn to communicate with your baby through song and signs in four simple sessions. The class is recommended for babies and toddlers 6 to 18 months.</p>
      <h3>Water Works!<br>Aqua Mom Fitness</h3>
      <p>Expecting moms and new moms: Water Works! Get a low-impact, low-intensity aqua workout to increase your energy and reduce fatigue. (Prenatal doctor's release required)</p>
      <h3>Parent &amp; Tot Aqua</h3>
      <p>Explore the water as a safe and fun environment for you and your child. In-water participation is required of a guardian or parent. Water activities progress based on individual readiness. Pre-registration is required. For children ages 1 to 3.</p>
    </div>
    <div class="column">
      <h3>Smart Sitter</h3>
      <p>Smart Sitter Basic is a medically accurate, hands-on, class that teaches boys and girls ages 11–13 how to handle emergencies when caring for children. This class teaches safe and nurturing child care techniques, behavior management skills and appropriate response to medical emergencies.</p>
      <h3>Child Passenger Safety</h3>
      <p>Motor vehicle crashes are the leading cause of injury-related death among children age 4 and under. Car seat checks by a Certified Child Passenger Safety Technician are available at all of our metro locations. Call to schedule an appointment.</p>
      <h3>Siblings for Life</h3>
      <p>This fun and interactive class emphasizes the role of the older sibling and helps prepare them to welcome their new brother or sister. For children ages 3-9.</p>
    </div>
  </div>
</section>

</body>
</html>
```